HTML Digital Sign layout and code (one page)...save us from the 60's!

Digital Sign for Headquarters Entrance

HTML Digital Sign layout (one page)...save us from the 60's!

Good Day Designers!

We have decided to install Digital Signage in our headquarters building that will replace the “felt boards” that the administrative staff use at our building entrances.

Instead of the information being displayed on the archaic sign boards, it will be presented on a landscaped 50inch LCD screen running at 1920x1080

We are looking for a one page HTML design that encompass the following elements:

+ Our Logo
+ Our Company Name (Vorlan Aerotek)
+ Our "Tag Line" - "Progress Shaped By Practice, Quality Shaped By Dedication"
+ Date and Time
+ A space for Today’s Birthdays (which could be up to 4 people)
+ A space for Today’s Anniversaries (which could be up to 4 people)
+ A space for Today’s Visitor (which could be up to 2 people)
+ A space for a Picture of the Day
+ A space for Weather Forecast (perhaps a graphic)
+ A small "banner" section or strip for scrolling Notices / Alerts (perhaps at the bottom of the page?)

The deliverables for the layout need to include the HTML, applicable CSS, HTML code, etc. We need this to be relatively turnkey.

I have included in the contest package a hi-res JPG and AI for our Company Logo.

From a color pallet perspective:

Light Blue:
RGB - 21, 191,242
HEX - #15BFF2

Dark Blue:
RGB - 0, 70, 154
HEX - #00469A

Additionally, I have done a contest like this before (for another company I was at) and have included a screen shot of that final display.

PLEASE NOTE: IT DOES NOT HAVE TO LOOK EXACTLY LIKE THE ATTACHED SCREEN SHOT FROM THE PREVIOUS CONTEST. Including the screenshot was just to give you a general idea of some inspiration and objectives.

Feedback and questions are encouraged.

Target Market(s)

Our Employees

Industry/Entity Type

Digital

Number of Pages Required

1 page

Requirements
Must have
• + Our Logo
• + Our Company Name (Vorlan Aerotek)
• + Our "Tag Line" - "Progress Shaped By Practice, Quality Shaped By Dedication"
• + Date and Time
• + A space for Today’s Birthdays (which could be up to 4 people)
• + A space for Today’s Anniversaries (which could be up to 4 people)
• + A space for Today’s Visitor (which could be up to 2 people)
• + A space for a Picture of the Day
• + A space for Weather Forecast (perhaps a graphic)
• + A small "banner" section or strip for scrolling Notices / Alerts (perhaps at the bottom of the page?)

```html
<!DOCTYPE html>
<html lang="en">
<head>
<meta charset="utf-8">
<title>Vorlan Aerotek – Entrance Display</title>
<link href="https://fonts.googleapis.com/css2?family=Fira+Sans+Condensed:wght@500;600&family=Lato:ital,wght@0,400;0,700;1,400&display=swap" rel="stylesheet">
<style>
  :root{
    --light-blue:#15BFF2;
    --dark-blue:#00469A;
    --royal:#0b3fc9;
    --panel-blue:#0a4fb0;
    --head-top:#1f78d6;
    --head-bottom:#0a4ea8;
    --tab:#0b5cc0;
    --row:#ececec;
    --ink:#222;
    --muted:#555;
    --white:#fff;
  }
  html,body{margin:0;padding:0;overflow:hidden;background:#0d1626;}
  .sign{position:relative;width:1200px;height:1089px;overflow:hidden;
    font-family:"Lato",sans-serif;
    background:linear-gradient(180deg,#1a2436 0%,#24304a 30%,#3a3a44 55%,#1c2234 80%,#141a28 100%);}
  .backdrop{position:absolute;left:0;top:372px;width:1200px;height:685px;
    background:radial-gradient(ellipse at 40% 30%,rgba(140,110,70,.35),transparent 60%),
               radial-gradient(ellipse at 80% 60%,rgba(90,110,160,.3),transparent 60%);}

  /* header */
  .sky{position:absolute;left:0;top:0;width:1200px;height:153px;
    background:linear-gradient(180deg,#8fd2f2 0%,#bfe6f8 60%,#e3f4fc 100%);}
  .brand{position:absolute;left:16px;top:22px;color:var(--royal);
    font-family:"Fira Sans Condensed",sans-serif;font-weight:600;line-height:1;}
  .brand-main{display:block;font-size:74px;letter-spacing:1px;}
  .brand-sub{display:block;font-size:20px;letter-spacing:13px;margin-top:6px;margin-left:8px;}

  .date-widget{position:absolute;left:975px;top:14px;width:175px;height:126px;
    background:#2f8fe8;border-radius:3px;box-shadow:0 0 0 1px #5aaaf0 inset;}
  .date-label{position:absolute;left:10px;top:9px;color:#fff;font:12px "Lato",sans-serif;display:flex;align-items:center;gap:6px;}
  .spinner{position:absolute;top:42px;width:44px;height:76px;border-radius:3px;
    background:linear-gradient(180deg,#d9d9d9 0,#f4f4f4 22%,#fff 23%,#fff 70%,#e6e6e6 71%,#cfcfcf 100%);
    font:18px "Lato",sans-serif;color:#222;text-align:center;}
  .spinner .plus,.spinner .minus{position:absolute;left:0;width:100%;color:#666;font-size:18px;line-height:1;}
  .spinner .plus{top:2px}
  .spinner .minus{bottom:2px}
  .spinner .val{position:absolute;left:0;width:100%;top:28px;}

  /* hero */
  .hero{position:absolute;left:13px;top:153px;width:1174px;height:219px;
    background:linear-gradient(90deg,#1a3fd0 0%,#2c6ce8 35%,#6a9fe6 55%,#2a3850 75%,#4a4a5a 100%);}
  .tagline{position:absolute;left:58px;margin:0;background:#fff;
    font-family:"Fira Sans Condensed",sans-serif;font-weight:600;font-size:37px;line-height:50px;padding:0 8px 0 8px;white-space:nowrap;}
  .tagline-1{top:63px;color:#0a1fa8;}
  .tagline-2{top:126px;color:#1c7fe6;}

  /* info cards */
  .card{position:absolute;top:413px;width:365px;}
  .card-head{position:relative;height:47px;background:linear-gradient(180deg,var(--head-top),var(--head-bottom));
    border-radius:3px 3px 0 0;}
  .card-tab{position:absolute;left:0;top:-3px;width:62px;height:50px;background:var(--tab);
    border-radius:3px 3px 0 0;display:flex;align-items:center;justify-content:center;box-shadow:2px 0 3px rgba(0,0,0,.3);}
  .card-title{position:absolute;left:76px;top:0;margin:0;line-height:50px;color:#fff;
    font-family:"Fira Sans Condensed",sans-serif;font-weight:500;font-size:30px;white-space:nowrap;}
  .card-title--long{font-size:27px;left:74px;}
  .card-list{list-style:none;margin:0;padding:0;background:var(--row);}
  .card-list li{height:43px;line-height:43px;border-bottom:1px dashed #9a9a9a;font-size:21.5px;color:var(--ink);padding-left:16px;white-space:nowrap;}
  .card-list li:last-child{border-bottom:none;}
  .num{display:inline-block;width:37px;color:var(--muted);font-family:"Fira Sans Condensed",sans-serif;font-weight:500;}

  /* picture of the day */
  .potd{position:absolute;left:13px;top:677px;width:770px;height:267px;}
  .potd-frame{position:absolute;left:0;top:0;}
  .potd-text{position:absolute;left:386px;top:14px;width:380px;color:#fff;}
  .potd-title{margin:0;display:flex;align-items:center;gap:14px;font-family:"Fira Sans Condensed",sans-serif;font-weight:500;font-size:28px;line-height:36px;
    padding-bottom:6px;border-bottom:1px solid rgba(255,255,255,.25);}
  .potd-title svg{flex:none;}
  .potd-sub{margin:10px 0 6px 14px;font-weight:700;font-size:19px;}
  .potd-body{margin:0 0 0 14px;font-size:13.4px;line-height:21.9px;}
  .potd-credit{margin:9px 0 0 14px;font-weight:700;font-size:16px;}
  .potd-credit em{font-weight:400;font-size:14.5px;}

  /* weather */
  .weather{position:absolute;left:821px;top:680px;width:366px;height:264px;}
  .weather .card-head{height:47px;}
  .weather-scene{position:absolute;left:0;top:47px;width:366px;height:217px;
    background:linear-gradient(180deg,#6a7a96 0%,#3c4a66 35%,#4a3a30 70%,#2a2630 100%);}
  .forecast{position:absolute;left:160px;top:30px;width:190px;height:148px;background:rgba(20,22,28,.82);color:#fff;}
  .forecast-temp{position:absolute;left:118px;top:20px;font-size:25px;}
  .forecast-temp sup{font-size:14px;}
  .forecast-city{position:absolute;left:107px;top:47px;font-size:19px;}
  .forecast-day{position:absolute;top:94px;width:60px;text-align:center;font-size:12.5px;line-height:26px;}
  .forecast-day span{display:block;border-top:1px solid rgba(255,255,255,.15);}

  /* notices */
  .notices{position:absolute;left:13px;top:976px;width:1174px;height:53px;overflow:hidden;
    background:linear-gradient(180deg,#fafafa,#dcdcdc);}
  .notices-band{position:absolute;left:0;top:0;}
  .notices-label{position:absolute;left:14px;top:0;line-height:53px;margin:0;color:#fff;
    font-family:"Fira Sans Condensed",sans-serif;font-weight:500;font-size:27px;}
  .notices-text{position:absolute;left:148px;top:0;margin:0;line-height:53px;font-size:22px;color:#222;white-space:nowrap;}

  /* footer */
  .footer{position:absolute;left:0;top:1057px;width:1200px;height:32px;background:var(--light-blue);
    color:#fff;font-size:12px;line-height:32px;}
  .footer .copy{position:absolute;left:14px;}
  .footer .web{position:absolute;right:15px;}
</style>
</head>
<body>
<main class="sign">
  <div class="backdrop" role="img" aria-label="Night skyline of a city seen from above"></div>

  <header class="sky">
    <div class="brand"><span class="brand-main">VORLAN</span><span class="brand-sub">AEROTEK</span></div>
    <div class="date-widget">
      <div class="date-label">
        <svg width="20" height="20" viewBox="0 0 20 20"><circle cx="10" cy="11" r="7.5" fill="none" stroke="#fff" stroke-width="1.6"/><rect x="8.5" y="1" width="3" height="2" fill="#fff"/><path d="M10 11 L13 7" stroke="#fff" stroke-width="1.6"/></svg>
        Thursday, April 13, 2014
      </div>
      <div class="spinner" style="left:10px"><span class="plus">+</span><span class="val">Apr</span><span class="minus">–</span></div>
      <div class="spinner" style="left:61px"><span class="plus">+</span><span class="val">12</span><span class="minus">–</span></div>
      <div class="spinner" style="left:112px;width:54px"><span class="plus">+</span><span class="val">2014</span><span class="minus">–</span></div>
    </div>
  </header>

  <section class="hero" role="img" aria-label="Train speeding past a subway platform in blue motion blur">
    <p class="tagline tagline-1">"PROGRESS SHAPED BY PRACTICE,</p>
    <p class="tagline tagline-2">QUALITY SHAPED BY DEDICATION"</p>
  </section>

  <section class="card" style="left:13px">
    <div class="card-head">
      <div class="card-tab">
        <svg width="34" height="32" viewBox="0 0 34 32" fill="#fff"><rect x="16" y="2" width="2" height="6"/><rect x="9" y="9" width="16" height="6"/><rect x="5" y="16" width="24" height="6"/><rect x="1" y="23" width="32" height="3"/><rect x="3" y="28" width="28" height="2"/></svg>
      </div>
      <h2 class="card-title">TODAY’S BIRTHDAYS</h2>
    </div>
    <ul class="card-list">
      <li><span class="num">(1)</span>Mr. Dorian Keel Marchetti</li>
      <li><span class="num">(2)</span>Mr. Evan Riso Talbrook</li>
      <li><span class="num">(3)</span>Mr. Nora Feliks Arden</li>
      <li><span class="num">(4)</span>Mr. Lena Corvin Hale</li>
    </ul>
  </section>

  <section class="card" style="left:417px">
    <div class="card-head">
      <div class="card-tab">
        <svg width="32" height="34" viewBox="0 0 32 34"><path d="M11 3 H21 L18 8 H14 Z" fill="#fff"/><circle cx="16" cy="20" r="10" fill="none" stroke="#fff" stroke-width="4"/></svg>
      </div>
      <h2 class="card-title card-title--long">TODAY’S ANNIVERSARIES</h2>
    </div>
    <ul class="card-list">
      <li><span class="num">(1)</span>Owen Patrick Reed And Mara</li>
      <li><span class="num">(2)</span>Cal Brennanston&nbsp; And Ivy</li>
      <li><span class="num">(3)</span>Grant&nbsp; Wellesby And Josephine</li>
      <li><span class="num">(4)</span>Milo Kastrovan And Tessa</li>
    </ul>
  </section>

  <section class="card" style="left:821px">
    <div class="card-head">
      <div class="card-tab">
        <svg width="32" height="34" viewBox="0 0 32 34" fill="#fff"><circle cx="16" cy="10" r="8"/><path d="M2 33 C2 22 8 19 16 19 C24 19 30 22 30 33 Z"/><path d="M16 20 L14 26 L16 31 L18 26 Z" fill="#0b5cc0"/></svg>
      </div>
      <h2 class="card-title">TODAY’S VISITOR</h2>
    </div>
    <ul class="card-list">
      <li><span class="num">(1)</span>Mr. Dorian Keel Marchetti</li>
      <li><span class="num">(2)</span>Mr. Evan Riso Talbrook</li>
      <li><span class="num">(3)</span>Mr. Nora Feliks Arden</li>
      <li><span class="num">(4)</span>Mr. Lena Corvin Hale</li>
    </ul>
  </section>

  <section class="potd">
    <svg class="potd-frame" width="770" height="267" viewBox="0 0 770 267">
      <defs>
        <linearGradient id="meadow" x1="0" y1="0" x2="0" y2="1">
          <stop offset="0" stop-color="#f2e7a0"/><stop offset="0.45" stop-color="#c9c25a"/><stop offset="0.75" stop-color="#6f8e2a"/><stop offset="1" stop-color="#3d5a16"/>
        </linearGradient>
      </defs>
      <rect x="0" y="0" width="770" height="267" fill="var(--panel-blue)"/>
      <path d="M0 0 H360 Q420 140 335 267 H0 Z" fill="var(--light-blue)"/>
      <path d="M0 0 H340 Q400 140 318 267 H0 Z" fill="#fff"/>
      <path d="M0 0 H300 Q380 140 310 267 H0 Z" fill="url(#meadow)" role="img" aria-label="Sunlit meadow with daisies and butterflies"/>
    </svg>
    <div class="potd-text">
      <h2 class="potd-title">
        <svg width="38" height="32" viewBox="0 0 38 32"><rect x="2" y="6" width="30" height="24" fill="none" stroke="#fff" stroke-width="2.5"/><path d="M6 2 H36 V24" fill="none" stroke="#fff" stroke-width="2"/><path d="M5 27 L14 16 L20 22 L24 18 L30 27 Z" fill="#fff"/><circle cx="24" cy="12" r="2.5" fill="#fff"/></svg>
        PICTURE OF THE DAY
      </h2>
      <p class="potd-sub">Picture Description:</p>
      <p class="potd-body">Lorem ipsum dolor sit amet, consectetur adipiscing elit. Nupo fermentum leo et odio luctus, at dignissim libero venenatis. Aliquam volutpat mi et ligula posuere dictum. Maecenas inam commodo dui at metus laci bibendum turpis tristique. oppoe Vivamus ut sem vitae felis placerat rhoncus q dignissim risus. Fusce diam nisl, hendrerit sit amet enim ut, ultrices sceleri.</p>
      <p class="potd-credit">Photo Credit: <em>Rafe Dunmore</em></p>
    </div>
  </section>

  <section class="weather">
    <div class="card-head">
      <div class="card-tab">
        <svg width="36" height="34" viewBox="0 0 36 34" fill="#fff"><circle cx="13" cy="11" r="5"/><g stroke="#fff" stroke-width="2"><path d="M13 1 V3 M4 11 H6 M6 4 L7.5 5.5 M20 4 L18.5 5.5"/></g><path d="M10 24 C6 24 6 17 11 17 C12 12 20 11 22 16 C27 14 31 18 29 22 C29 24 27 24 26 24 Z"/><g><circle cx="13" cy="29" r="1.5"/><circle cx="19" cy="29" r="1.5"/><circle cx="25" cy="29" r="1.5"/></g></svg>
      </div>
      <h2 class="card-title" style="left:82px">WEATHER FORECAST</h2>
    </div>
    <div class="weather-scene" role="img" aria-label="Evening view over a city with a lattice tower">
      <div class="forecast">
        <svg style="position:absolute;left:12px;top:8px" width="96" height="84" viewBox="0 0 96 84">
          <g stroke="#f5a21a" stroke-width="5" stroke-linecap="round"><path d="M42 4 V12 M20 14 L26 20 M64 14 L58 20 M12 36 H20"/></g>
          <circle cx="42" cy="38" r="16" fill="#f5a21a"/>
          <path d="M34 66 C24 66 24 52 35 52 C37 42 52 40 56 48 C64 44 76 50 72 60 C78 62 76 66 72 66 Z" fill="#e8ecf0"/>
          <path d="M52 64 L44 78 H52 L46 90" fill="none" stroke="#f3d21c" stroke-width="4"/>
        </svg>
        <div class="forecast-temp">27 <sup>o</sup>F</div>
        <div class="forecast-city">London</div>
        <div class="forecast-day" style="left:30px">Mon<span>75/23 <sup>o</sup>F</span></div>
        <div class="forecast-day" style="left:110px">Tue<span>75/23 <sup>o</sup>F</span></div>
      </div>
    </div>
  </section>

  <section class="notices">
    <svg class="notices-band" width="160" height="53" viewBox="0 0 160 53"><polygon points="0,0 160,0 136,53 0,53" fill="#1565c0"/></svg>
    <h2 class="notices-label">NOTICES</h2>
    <p class="notices-text">Lorem ipsum dolor sit amet, consectetur adipiscing elit. Vestibulum id tincidunt ex. Integer sollcitudin</p>
  </section>

  <footer class="footer">
    <span class="copy">© 2014 VORLAN AEROTEK. ALL RIGHTS RESERVED</span>
    <span class="web">WWW.VORLANAERO.COM</span>
  </footer>
</main>
</body>
</html>
```